Equine Horse Employment site

We need to redesign the layout of Stablemark Hire.co.uk

It will offer Job seekers and Employers the place to look for a job, and look for a candidate.

The logical format needs to be improved and the layout must look highly visually appealing.

It needs to be incredibly simple to use and one click access to any part of the site.

The homepage must convey the following

- Log in and register areas
- Current Job Listings
- Current CV's
- Exclusive Service Club button
- Search box to allow simple searching for Jobs or CVs

We need PSD layouts for Homepage, Job listing Page, CV listing Page, Job Profile and CV Profile. This job is for the design of 5 PSD screens.

Generic page for ancillary page such as about, contact and news.

The biggest competitor is PaddockPost.com

Please ask us any questions and please be prepared to make changes, as we are very particular.

More work will be provided to the winning designer.

thanks

• It must not look cheap or like a job board, it has to have character and feel friendly, and inviting. Please do not submit poor designs that look like a job board, as they will be rejected instantly.

thanks

```html
<!DOCTYPE html>
<html lang="en">
<head>
<meta charset="utf-8">
<title>Stablemark Hire – Equestrian Recruitment Specialists</title>
<link href="https://fonts.googleapis.com/css2?family=Questrial&family=Arimo:wght@400;700&family=Oswald:wght@400&display=swap" rel="stylesheet">
<style>
:root{
  --header-green:#7b9a5c;
  --header-light:#9fb884;
  --mint:#badcc2;
  --olive-text:#7a9a52;
  --job-green:#2f9a48;
  --ink:#1f2a18;
  --body-text:#222;
  --meta-text:#333;
  --divider:#cfcfcf;
  --white:#ffffff;
  --footer-text:#eef3e6;
  --footer-muted:#dfe8d3;
  --badge-dark:#3b3b3b;
  --badge-grey:#9a9a9a;
  --button-grey:#6b7a66;
}
*{margin:0;padding:0;box-sizing:border-box}
html,body{width:1084px;height:1200px;overflow:hidden;background:var(--white)}
body{position:relative;font-family:"Arimo",Arial,sans-serif;color:var(--body-text)}
.abs{position:absolute}

/* header */
.site-header{position:absolute;left:0;top:0;width:1084px;height:177px;
  background:radial-gradient(ellipse 380px 120px at 542px 90px,var(--header-light),var(--header-green) 100%)}
.account-links{position:absolute;top:12px;left:766px;display:flex;gap:16px;font-size:9px;color:var(--footer-text)}
.account-links span{display:flex;align-items:center;gap:4px}
.brand{position:absolute;left:0;width:1084px;top:78px;text-align:center}
.brand-name{font-family:"Questrial",sans-serif;font-size:31px;letter-spacing:2px;color:var(--ink)}
.brand-tag{font-size:9px;color:var(--ink);margin-top:2px}
.main-nav{position:absolute;top:152px;left:0;width:1084px;font-family:"Questrial",sans-serif;color:var(--ink);font-size:15px}
.main-nav span{position:absolute;transform:translateX(-50%);white-space:nowrap}
.main-nav .current{font-size:21px;top:-5px}

/* search band */
.search-band{position:absolute;left:0;top:177px;width:1084px;height:129px;background:var(--mint)}
.club{position:absolute;top:15px;left:0;width:1084px;text-align:center;font-family:"Oswald",sans-serif;font-size:13px;letter-spacing:.5px;color:var(--olive-text)}
.search-panel{position:absolute;top:40px;width:230px}
.search-panel h2{font-family:"Questrial",sans-serif;font-weight:400;font-size:22px;color:var(--olive-text);text-align:center}
.search-options{display:flex;justify-content:center;gap:24px;font-size:11px;color:var(--olive-text);margin-top:5px;font-family:"Questrial",sans-serif}
.search-options span{display:flex;align-items:center;gap:4px}
.box{width:8px;height:8px;border:1px solid #777;background:#fff;display:inline-block;position:relative}
.box.on::after{content:"";position:absolute;left:1px;top:1px;width:4px;height:4px;background:#333}
.search-field{display:flex;margin-top:5px;margin-left:5px}
.search-field input{width:192px;height:17px;border:none;font-size:8px;padding-left:5px;font-family:"Arimo",sans-serif;color:#555}
.search-field .go{width:17px;height:17px;background:#8aa276;display:flex;align-items:center;justify-content:center}
.adv{font-size:6px;color:#3f7fae;text-decoration:underline;text-align:right;margin-right:10px;margin-top:1px}

/* listings */
.column-title{position:absolute;top:318px;width:260px;text-align:center;font-family:"Questrial",sans-serif;font-size:18px;color:var(--olive-text)}
.column-title::after{content:"";display:block;height:1px;margin-top:3px;background:linear-gradient(90deg,transparent,#cdd6c4,transparent)}
.listing{position:absolute;width:400px;height:70px}
.listing .photo{position:absolute;left:0;top:0;width:63px;height:63px;background:linear-gradient(180deg,#8fa36f 0%,#6f8a5a 50%,#b8b8b8 100%)}
.listing h3{position:absolute;left:77px;top:2px;font-family:"Questrial",sans-serif;font-weight:400;font-size:15px;color:var(--job-green)}
.listing p{position:absolute;left:77px;top:25px;width:165px;font-size:8.5px;line-height:11px;color:var(--body-text)}
.listing .rule{position:absolute;left:256px;top:2px;width:1px;height:56px;background:var(--divider)}
.listing .meta{position:absolute;left:265px;font-size:7.5px;color:var(--meta-text);display:flex;align-items:center;gap:8px}

/* partners */
.partners{position:absolute;top:1010px;left:0;width:1084px;height:48px}
.partners .label{position:absolute;left:229px;top:17px;font-size:10px;color:var(--job-green)}

/* footer */
.site-footer{position:absolute;left:0;top:1069px;width:1084px;height:131px;background:var(--header-green);color:var(--footer-text)}
.footer-nav{position:absolute;top:9px;left:0;width:1084px;text-align:center;font-size:9.5px}
.footer-nav .sep{margin:0 8px}
.footer-brand{position:absolute;left:214px;top:70px;font-family:"Questrial",sans-serif;font-size:14px;color:var(--footer-muted);opacity:.8}
.copyright{position:absolute;left:171px;top:103px;font-size:8px;color:var(--footer-muted)}
.social{position:absolute;left:374px;top:46px;display:flex;gap:5px}
.social span{width:15px;height:15px;background:var(--footer-muted);opacity:.75;border-radius:2px}
.about{position:absolute;left:374px;top:69px;width:290px;font-size:8px;line-height:10.5px;color:var(--footer-muted)}
.newsletter{position:absolute;left:725px;top:54px;width:180px}
.newsletter .label{font-size:9px;margin-left:6px}
.newsletter .email{margin-top:2px;height:20px;background:#fff;border:1px solid #c8d3bd;font-size:11px;color:#777;padding:3px 6px}
.newsletter .subscribe{margin:5px 0 0 122px;width:58px;height:16px;background:var(--button-grey);border-radius:2px;font-size:9px;text-align:center;line-height:16px;color:#fff}
</style>
</head>
<body>

<header class="site-header">
  <div class="account-links">
    <span><svg width="9" height="10" viewBox="0 0 9 10"><rect x="1" y="4" width="7" height="6" fill="#eef3e6"/><path d="M2.5 4V2.8a2 2 0 0 1 4 0V4" stroke="#eef3e6" fill="none" stroke-width="1.2"/></svg>Login</span>
    <span><svg width="12" height="10" viewBox="0 0 12 10"><circle cx="5" cy="3" r="2.2" fill="#eef3e6"/><path d="M1 10a4 3.4 0 0 1 8 0z" fill="#eef3e6"/><path d="M9.5 2v4M7.5 4h4" stroke="#eef3e6" stroke-width="1.2"/></svg>Register</span>
  </div>
  <div class="brand">
    <div class="brand-name">STABLEMARK HIRE</div>
    <div class="brand-tag">Equestrian Recruitment Specialists</div>
  </div>
  <nav class="main-nav">
    <span style="left:276px">JOB PROFILE</span>
    <span style="left:411px">JOB LISTING</span>
    <span class="current" style="left:542px">HOME</span>
    <span style="left:671px">CV LISTING</span>
    <span style="left:805px">CV PROFILE</span>
  </nav>
</header>

<section class="search-band">
  <div class="club">EXCLUSIVE SERVICE CLUB</div>
  <div class="search-panel" style="left:224px">
    <h2>Looking for Job</h2>
    <div class="search-options"><span><i class="box on"></i>Job type</span><span><i class="box"></i>Location</span></div>
    <div class="search-field"><input value="Enter Keywords" readonly><div class="go"><svg width="10" height="10" viewBox="0 0 10 10"><circle cx="4" cy="4" r="2.8" stroke="#fff" fill="none" stroke-width="1.3"/><path d="M6 6l3 3" stroke="#fff" stroke-width="1.5"/></svg></div></div>
    <div class="adv">Adv Search</div>
  </div>
  <div class="search-panel" style="left:627px">
    <h2>Looking for Staff</h2>
    <div class="search-options"><span><i class="box on"></i>Staff type</span><span><i class="box"></i>Location</span></div>
    <div class="search-field"><input value="Enter Keywords" readonly><div class="go"><svg width="10" height="10" viewBox="0 0 10 10"><circle cx="4" cy="4" r="2.8" stroke="#fff" fill="none" stroke-width="1.3"/><path d="M6 6l3 3" stroke="#fff" stroke-width="1.5"/></svg></div></div>
    <div class="adv">Adv Search</div>
  </div>
</section>

<div class="column-title" style="left:208px">Featured Jobs</div>
<div class="column-title" style="left:611px">Featured Cv’s</div>

<svg width="0" height="0" style="position:absolute">
  <defs>
    <symbol id="pin" viewBox="0 0 8 11"><path d="M4 0a3.2 3.2 0 0 1 3.2 3.2C7.2 5.5 4 11 4 11S.8 5.5.8 3.2A3.2 3.2 0 0 1 4 0z" fill="#6b7d55"/><circle cx="4" cy="3.2" r="1.2" fill="#fff"/></symbol>
    <symbol id="clock" viewBox="0 0 10 10"><circle cx="5" cy="5" r="4.6" fill="#8a9a72"/><path d="M3 5.2l1.5 1.5L7.3 3.6" stroke="#fff" stroke-width="1.2" fill="none"/></symbol>
  </defs>
</svg>

<!-- featured jobs -->
<div class="listing" style="left:160px;top:368px"><div class="photo" role="img" aria-label="Photo of a riding instructor on horseback"></div><h3>Instructor Rider</h3><p>We are looking for an instructor that can work for<br>us from 1 September ...</p><div class="rule"></div><div class="meta" style="top:4px"><svg width="7" height="10"><use href="#pin"/></svg>Where it is</div><div class="meta" style="top:24px"><svg width="10" height="10"><use href="#clock"/></svg>Posted 28. Jun, 2012</div></div>
<div class="listing" style="left:160px;top:455px"><div class="photo" role="img" aria-label="Photo of a riding instructor on horseback"></div><h3>Instructor Rider</h3><p>We are looking for an instructor that can work for<br>us from 1 September ...</p><div class="rule"></div><div class="meta" style="top:4px"><svg width="7" height="10"><use href="#pin"/></svg>Where it is</div><div class="meta" style="top:24px"><svg width="10" height="10"><use href="#clock"/></svg>Posted 28. Jun, 2012</div></div>
<div class="listing" style="left:160px;top:543px"><div class="photo" role="img" aria-label="Photo of a riding instructor on horseback"></div><h3>Instructor Rider</h3><p>We are looking for an instructor that can work for<br>us from 1 September ...</p><div class="rule"></div><div class="meta" style="top:4px"><svg width="7" height="10"><use href="#pin"/></svg>Where it is</div><div class="meta" style="top:24px"><svg width="10" height="10"><use href="#clock"/></svg>Posted 28. Jun, 2012</div></div>
<div class="listing" style="left:160px;top:630px"><div class="photo" role="img" aria-label="Photo of a riding instructor on horseback"></div><h3>Instructor Rider</h3><p>We are looking for an instructor that can work for<br>us from 1 September ...</p><div class="rule"></div><div class="meta" style="top:4px"><svg width="7" height="10"><use href="#pin"/></svg>Where it is</div><div class="meta" style="top:24px"><svg width="10" height="10"><use href="#clock"/></svg>Posted 28. Jun, 2012</div></div>
<div class="listing" style="left:160px;top:717px"><div class="photo" role="img" aria-label="Photo of a riding instructor on horseback"></div><h3>Instructor Rider</h3><p>We are looking for an instructor that can work for<br>us from 1 September ...</p><div class="rule"></div><div class="meta" style="top:4px"><svg width="7" height="10"><use href="#pin"/></svg>Where it is</div><div class="meta" style="top:24px"><svg width="10" height="10"><use href="#clock"/></svg>Posted 28. Jun, 2012</div></div>
<div class="listing" style="left:160px;top:805px"><div class="photo" role="img" aria-label="Photo of a riding instructor on horseback"></div><h3>Instructor Rider</h3><p>We are looking for an instructor that can work for<br>us from 1 September ...</p><div class="rule"></div><div class="meta" style="top:4px"><svg width="7" height="10"><use href="#pin"/></svg>Where it is</div><div class="meta" style="top:24px"><svg width="10" height="10"><use href="#clock"/></svg>Posted 28. Jun, 2012</div></div>
<div class="listing" style="left:160px;top:892px"><div class="photo" role="img" aria-label="Photo of a riding instructor on horseback"></div><h3>Instructor Rider</h3><p>We are looking for an instructor that can work for<br>us from 1 September ...</p><div class="rule"></div><div class="meta" style="top:4px"><svg width="7" height="10"><use href="#pin"/></svg>Where it is</div><div class="meta" style="top:24px"><svg width="10" height="10"><use href="#clock"/></svg>Posted 28. Jun, 2012</div></div>

<!-- featured cvs -->
<div class="listing" style="left:563px;top:368px"><div class="photo" role="img" aria-label="Photo of a riding instructor on horseback"></div><h3>Instructor Rider</h3><p>We are looking for an instructor that can work for<br>us from 1 September ...</p><div class="rule"></div><div class="meta" style="top:4px"><svg width="7" height="10"><use href="#pin"/></svg>Where it is</div><div class="meta" style="top:24px"><svg width="10" height="10"><use href="#clock"/></svg>Posted 28. Jun, 2012</div></div>
<div class="listing" style="left:563px;top:455px"><div class="photo" role="img" aria-label="Photo of a riding instructor on horseback"></div><h3>Instructor Rider</h3><p>We are looking for an instructor that can work for<br>us from 1 September ...</p><div class="rule"></div><div class="meta" style="top:4px"><svg width="7" height="10"><use href="#pin"/></svg>Where it is</div><div class="meta" style="top:24px"><svg width="10" height="10"><use href="#clock"/></svg>Posted 28. Jun, 2012</div></div>
<div class="listing" style="left:563px;top:543px"><div class="photo" role="img" aria-label="Photo of a riding instructor on horseback"></div><h3>Instructor Rider</h3><p>We are looking for an instructor that can work for<br>us from 1 September ...</p><div class="rule"></div><div class="meta" style="top:4px"><svg width="7" height="10"><use href="#pin"/></svg>Where it is</div><div class="meta" style="top:24px"><svg width="10" height="10"><use href="#clock"/></svg>Posted 28. Jun, 2012</div></div>
<div class="listing" style="left:563px;top:630px"><div class="photo" role="img" aria-label="Photo of a riding instructor on horseback"></div><h3>Instructor Rider</h3><p>We are looking for an instructor that can work for<br>us from 1 September ...</p><div class="rule"></div><div class="meta" style="top:4px"><svg width="7" height="10"><use href="#pin"/></svg>Where it is</div><div class="meta" style="top:24px"><svg width="10" height="10"><use href="#clock"/></svg>Posted 28. Jun, 2012</div></div>
<div class="listing" style="left:563px;top:717px"><div class="photo" role="img" aria-label="Photo of a riding instructor on horseback"></div><h3>Instructor Rider</h3><p>We are looking for an instructor that can work for<br>us from 1 September ...</p><div class="rule"></div><div class="meta" style="top:4px"><svg width="7" height="10"><use href="#pin"/></svg>Where it is</div><div class="meta" style="top:24px"><svg width="10" height="10"><use href="#clock"/></svg>Posted 28. Jun, 2012</div></div>
<div class="listing" style="left:563px;top:805px"><div class="photo" role="img" aria-label="Photo of a riding instructor on horseback"></div><h3>Instructor Rider</h3><p>We are looking for an instructor that can work for<br>us from 1 September ...</p><div class="rule"></div><div class="meta" style="top:4px"><svg width="7" height="10"><use href="#pin"/></svg>Where it is</div><div class="meta" style="top:24px"><svg width="10" height="10"><use href="#clock"/></svg>Posted 28. Jun, 2012</div></div>
<div class="listing" style="left:563px;top:892px"><div class="photo" role="img" aria-label="Photo of a riding instructor on horseback"></div><h3>Instructor Rider</h3><p>We are looking for an instructor that can work for<br>us from 1 September ...</p><div class="rule"></div><div class="meta" style="top:4px"><svg width="7" height="10"><use href="#pin"/></svg>Where it is</div><div class="meta" style="top:24px"><svg width="10" height="10"><use href="#clock"/></svg>Posted 28. Jun, 2012</div></div>

<section class="partners" aria-label="Partners">
  <span class="label">we work with</span>
  <svg class="abs" style="left:310px;top:0" width="470" height="46" viewBox="0 0 470 46" role="img" aria-label="Partner badges">
    <circle cx="23" cy="21" r="17" fill="#8a8a8a"/>
    <rect x="63" y="10" width="117" height="22" fill="var(--badge-dark)"/>
    <circle cx="219" cy="20" r="16" fill="#cfcfcf"/>
    <rect x="263" y="11" width="116" height="22" fill="var(--badge-grey)"/>
    <rect x="412" y="1" width="49" height="39" fill="#555"/>
  </svg>
</section>

<footer class="site-footer">
  <nav class="footer-nav">Home<span class="sep">|</span>About Stablemark Hire<span class="sep">|</span>Equine Job Seekers<span class="sep">|</span>Equine Employers<span class="sep">|</span>Equine Industry News<span class="sep">|</span>Equestrian Resources<span class="sep">|</span>Webmasters<span class="sep">|</span>Login<span class="sep">|</span>Sitemap</nav>
  <div class="footer-brand">STABLEMARK HIRE</div>
  <div class="copyright">© 2006–2012, Stablemark Hire | All Rights Reserved</div>
  <div class="social"><span></span><span></span><span></span></div>
  <p class="about">Equestrian Jobs at Stablemark Hire. A precise way for equine job seekers and employers to conduct a search for qualified candidates and jobs. No1 in search and a reach of over 500,000 users in the UK alone. Now partnered with Swapboard providing greater reach to the best talent in Europe.</p>
  <div class="newsletter">
    <div class="label">Subscribe to the Newsletter</div>
    <div class="email">Enter Email Address</div>
    <div class="subscribe">Subscribe</div>
  </div>
</footer>

</body>
</html>
```